BUSINESS CARD - HALVERDINE RURAL SERVICES

I would like to create a business card for my fertilizer spreading business. I would like to incorporate my existing logo and also a description of the services offered. The business card will be given to farmers so must be kept simple but effective. It will also be left in stores so much also be eye catching in order to stand out from other cards.

Target Market(s)

FARMERS

Requirements
Must have
• FRONT OF CARD = EXISTING LOGO + "CUSTOMISED SPREADING" below the logo

REAR Of CARD = SERVICES OFFERED AND CONTACT DETAILS

- Bulk fertilizer including Lime, Gypsum, Manure & Compost
- Granular fertilizer including Single Super, Urea, Gran-am, & Custom Blends
- Modern equipment - Autosteer & Variable Rate Capable
- Friendly & Reliable Service
- Contact Gus: 0471 502 318
Nice to have
• utilize same color scheme as existing logo

```html
<!DOCTYPE html>
<html lang="en">
<head>
<meta charset="utf-8">
<title>Halverdine Rural Services – Business Card</title>
<link href="https://fonts.googleapis.com/css2?family=Lato:wght@400;700&display=swap" rel="stylesheet">
<style>
  :root {
    --page-bg: #efeeef;
    --card-light: #ffffff;
    --card-dark: #222222;
    --ink-grey: #575757;
    --ink-white: #ffffff;
    --accent-orange: #f39322;
  }
  * { box-sizing: border-box; margin: 0; padding: 0; }
  html, body {
    width: 1146px;
    height: 1200px;
    overflow: hidden;
    background: var(--page-bg);
    font-family: "Lato", sans-serif;
  }
  .canvas { position: relative; width: 1146px; height: 1200px; }
  .card {
    position: absolute;
    left: 190px;
    width: 764px;
    height: 440px;
    border-radius: 28px;
    overflow: hidden;
  }
  .card--front { top: 153px; background: var(--card-light); }
  .card--back { top: 636px; background: var(--card-dark); }

  /* Brand block: plain circle + name */
  .brand {
    position: absolute;
    display: flex;
    flex-direction: column;
    align-items: center;
    text-align: center;
  }
  .brand__dot { border-radius: 50%; }
  .brand__name { font-weight: 700; line-height: 1.1; letter-spacing: -0.3px; white-space: nowrap; }

  .card--front .brand { left: 392px; top: 55px; width: 236px; }
  .card--front .brand__dot { width: 106px; height: 106px; background: var(--ink-grey); margin-bottom: 12px; }
  .card--front .brand__name { color: var(--ink-grey); font-size: 21px; }

  .card--back .brand { left: 182px; top: 54px; width: 400px; }
  .card--back .brand__dot { width: 128px; height: 128px; background: var(--ink-white); margin-bottom: 14px; }
  .card--back .brand__name { color: var(--ink-white); font-size: 28px; }
  .brand__tagline {
    margin-top: 8px;
    color: var(--accent-orange);
    font-size: 15px;
    font-weight: 700;
    letter-spacing: 3px;
  }

  /* Person + contact */
  .person { position: absolute; left: 47px; top: 306px; }
  .person__name { color: var(--accent-orange); font-size: 28px; font-weight: 700; line-height: 1.1; }
  .person__role { color: var(--ink-grey); font-size: 19px; line-height: 1.3; }
  .person__contact {
    display: flex;
    align-items: center;
    gap: 7px;
    margin-top: 8px;
    color: var(--ink-grey);
    font-size: 16px;
  }
  .person__contact svg { width: 15px; height: 15px; fill: var(--accent-orange); }

  /* Services list */
  .services { position: absolute; left: 392px; top: 232px; width: 350px; color: var(--ink-grey); }
  .services__title {
    display: inline-block;
    font-size: 20px;
    font-weight: 400;
    letter-spacing: 0.2px;
    padding-bottom: 2px;
    border-bottom: 2px solid var(--accent-orange);
    margin-bottom: 10px;
  }
  .services__list { list-style: none; font-size: 16px; line-height: 20px; }
  .services__list li { position: relative; padding-left: 18px; margin-bottom: 4px; }
  .services__list li::before {
    content: "";
    position: absolute;
    left: 0;
    top: 6px;
    width: 8px;
    height: 8px;
    border-radius: 50%;
    background: var(--accent-orange);
  }

  .services-centered {
    position: absolute;
    left: 0;
    right: 0;
    top: 299px;
    list-style: none;
    text-align: center;
    color: var(--ink-white);
    font-size: 17px;
    line-height: 23.5px;
  }
</style>
</head>
<body>
<main class="canvas">
  <section class="card card--front">
    <div class="brand">
      <span class="brand__dot"></span>
      <span class="brand__name">Halverdine Rural Services</span>
    </div>

    <div class="person">
      <p class="person__name">Gus Whitcombe</p>
      <p class="person__role">Co-founder</p>
      <p class="person__contact">
        <svg viewBox="0 0 24 24" aria-hidden="true"><path d="M6.6 10.8a15.1 15.1 0 0 0 6.6 6.6l2.2-2.2a1 1 0 0 1 1-.25 11.4 11.4 0 0 0 3.6.57 1 1 0 0 1 1 1V20a1 1 0 0 1-1 1A17 17 0 0 1 3 4a1 1 0 0 1 1-1h3.5a1 1 0 0 1 1 1c0 1.25.2 2.45.57 3.57a1 1 0 0 1-.25 1z"/></svg>
        Contact Gus: 0471 502 318
      </p>
    </div>

    <div class="services">
      <h2 class="services__title">SERVICES OFFERED</h2>
      <ul class="services__list">
        <li>Modern equipment</li>
        <li>Friendly &amp; Reliable Services</li>
        <li>Bulk fertilizer including Lime,<br>Gypsum, Manure &amp; Composts</li>
        <li>Granular fertilizer including Single Super,<br>Urea, Gran-am, &amp; Custom Blends</li>
      </ul>
    </div>
  </section>

  <section class="card card--back">
    <div class="brand">
      <span class="brand__dot"></span>
      <span class="brand__name">Halverdine Rural Services</span>
      <span class="brand__tagline">CUSTOMISED SPREADING</span>
    </div>
    <ul class="services-centered">
      <li>Modern equipment</li>
      <li>Friendly &amp; Reliable Services</li>
      <li>Bulk fertilizer including Lime, Gypsum, Manure &amp; Composts</li>
      <li>Granular fertilizer including Single Super, Urea, Gran-am, &amp; Custom Blends</li>
    </ul>
  </section>
</main>
</body>
</html>
```